BRIGHTMERE WINE LABEL RANGE PROJECT

We need an elegant wine label design for our new range of wine. We need 3 labels for the range

2015 Brightmere Shiraz
2015 Brightmere Cabernet
2015 Brightmere Shiraz Cabernet

The Size is nominated at 120mm High x 70mm Wide (Front and Back) but we are open to creative expression even if size differs

We are open to any style of label and designer can work on their strengths. it can be modern/classic/old fashion etc

I will attach the tasting notes which shows the title of wine for front label and tasting notes and details to be included at back. Please leave space for a barcode.

Thanks
Tomas.

Target Market(s)

WINE DRINKERS 35-65

Requirements
Must have
• ELEGANCE

Files

```html
<!DOCTYPE html>
<html lang="en">
<head>
<meta charset="utf-8">
<title>Brightmere Shiraz Cabernet – Label Range</title>
<link rel="stylesheet" href="https://fonts.googleapis.com/css2?family=Marcellus+SC&family=Open+Sans:wght@400&display=swap">
<style>
  :root {
    --page: #ffffff;
    --label-black: #1d1d1d;
    --label-white: #ffffff;
    --ink-light: #e6e6e6;
    --ink-dark: #2a2a2a;
    --plum: #4b1a4d;
    --plum-soft: #6a3a6c;
    --vine-green: #6cbb2d;
    --leaf-soft: #8fd06a;
    --shadow: rgba(0,0,0,0.22);
  }
  * { margin: 0; padding: 0; box-sizing: border-box; }
  html, body { width: 1200px; height: 849px; overflow: hidden; background: var(--page); }
  .canvas { position: relative; width: 1200px; height: 849px; }

  .label {
    position: absolute;
    box-shadow: 0 0 4px var(--shadow);
    text-align: center;
  }
  .label--white { background: var(--label-white); color: var(--ink-dark); }
  .label--black { background: var(--label-black); color: var(--ink-light); }

  .caps { font-family: "Marcellus SC", serif; letter-spacing: 0.04em; line-height: 1.25; }

  .illustration {
    position: absolute;
    background: linear-gradient(180deg, var(--plum-soft) 0%, var(--plum) 55%, var(--leaf-soft) 100%);
    opacity: 0.85;
  }

  .notes {
    font-family: "Open Sans", sans-serif;
    font-size: 7.4px;
    line-height: 1.33;
    text-align: justify;
    text-align-last: center;
  }
  .notes p + p { margin-top: 9px; }

  /* Top row */
  .front-art-top { left: 32px; top: 54px; width: 200px; height: 250px; }
  .front-art-top .illustration { left: 12px; top: 50px; width: 176px; height: 164px; }

  .title-band { left: 32px; top: 311px; width: 200px; height: 87px; padding-top: 8px; }
  .title-band .year, .title-band .place { font-size: 11px; }
  .title-band .varietal { font-size: 18.5px; margin-top: 1px; line-height: 1.1; }
  .title-band .volume { font-size: 10px; }

  .back-notes-top { left: 264px; top: 54px; width: 201px; height: 250px; padding: 14px 12px 0; }

  .spec-card { left: 264px; top: 311px; width: 201px; height: 87px; padding-top: 25px; font-size: 10.5px; line-height: 1.15; }

  /* Bottom row */
  .front-full { left: 32px; top: 444px; width: 200px; height: 343px; }
  .front-full .illustration { left: 8px; top: 28px; width: 184px; height: 196px; }
  .front-full .title { position: absolute; left: 0; right: 0; top: 262px; }
  .front-full .year, .front-full .place, .front-full .volume { color: var(--vine-green); font-size: 11.5px; }
  .front-full .varietal { color: var(--plum); font-size: 18.5px; line-height: 1.1; }

  .back-full { left: 265px; top: 444px; width: 200px; height: 343px; padding: 32px 12px 0; }
  .back-full .spec { position: absolute; left: 0; right: 0; top: 280px; font-size: 10.5px; line-height: 1.15; }
</style>
</head>
<body>
<main class="canvas">

  <section class="label label--white front-art-top">
    <div class="illustration" role="img" aria-label="Illustration area: hand-drawn purple plum with a green stem and leaf"></div>
  </section>

  <section class="label label--black title-band caps">
    <div class="year">2015</div>
    <div class="place">Brightmere</div>
    <div class="place">South Australian</div>
    <div class="varietal">Shiraz Cabernet</div>
    <div class="volume">750ml</div>
  </section>

  <section class="label label--black back-notes-top notes">
    <p>The 2015 Shiraz has a colour of crimson red and maroon and imparts a spicy, berry aroma.</p>
    <p>The berry fruit lift of blackcurrant and plums is complemented by underlying cigar box and tobacco leaf aromas. The palate is fresh and fruit driven with soft leathery tannins.</p>
    <p>The length of the wine is middle weight with long lasting flavours which are endearing qualities indicative of what the vineyard delivers each year. Low yielding vines along with cool nights and slow ripening in the vineyard are major factors contributing to this wonderful wine.</p>
    <p>The wine is a fine example of the variety of Shiraz and will complement foods with richness and savoury finishes, which will match with a variety of selected meats, including poultry.</p>
    <p>The wine will cellar for 5 years or more and mature into an excellent example of a typical South Australian Shiraz.</p>
  </section>

  <section class="label label--white spec-card caps">
    <div>Alcohol : 14.0%</div>
    <div>Standard Drinks : 8.3</div>
    <div>Wine of Australia</div>
  </section>

  <section class="label label--white front-full caps">
    <div class="illustration" role="img" aria-label="Illustration area: hand-drawn purple plum with a green stem and leaf"></div>
    <div class="title">
      <div class="year">2015</div>
      <div class="place">Brightmere</div>
      <div class="place">South Australian</div>
      <div class="varietal">Shiraz Cabernet</div>
      <div class="volume">750ml</div>
    </div>
  </section>

  <section class="label label--black back-full">
    <div class="notes">
      <p>The 2015 Shiraz has a colour of crimson red and maroon and imparts a spicy, berry aroma.</p>
      <p>The berry fruit lift of blackcurrant and plums is complemented by underlying cigar box and tobacco leaf aromas. The palate is fresh and fruit driven with soft leathery tannins.</p>
      <p>The length of the wine is middle weight with long lasting flavours which are endearing qualities indicative of what the vineyard delivers each year. Low yielding vines along with cool nights and slow ripening in the vineyard are major factors contributing to this wonderful wine.</p>
      <p>The wine is a fine example of the variety of Shiraz and will complement foods with richness and savoury finishes, which will match with a variety of selected meats, including poultry.</p>
      <p>The wine will cellar for 5 years or more and mature into an excellent example of a typical South Australian Shiraz.</p>
    </div>
    <div class="spec caps">
      <div>Alcohol : 14.0%</div>
      <div>Standard Drinks : 8.3</div>
      <div>Wine of Australia</div>
    </div>
  </section>

</main>
</body>
</html>
```